New Peanut Butter Brand Needs Product Label

We need a packaging label for a new to market peanut butter product based in the UK. The range of peanut butters will include a range of great flavours. We have been looking at labels to give inspiration and we are liking the less complicated designs that are on a white background (Sample designs are attached).

The company is called 'Breezy Acorn Company' The name could be used in full or shortened to 'Breezy Acorn Co'

The design should be a little fun and cool (not in a childish way), using bright colours and a mixture of fonts would be fine (as long as the text is easy to read)

For the purposes of this design brief text that should be added to the front of the design is

Brand name (As above)
Sea Salt (The flavour of this product)
Chunky (Peanut butter is chunky or smooth right !!)

Allowance should be given for the ingredients panel and standard information used on a food product.

Key phrases that could be used in the design are below

Great source of protein
Heart Healthy
Packed with nutrients

The food container will be a plastic pot and so the labels are slightly curved. I have attached a picture of a similar pot and a label outline an sizing which should be of help.

```html
<!DOCTYPE html>
<html lang="en">
<head>
<meta charset="utf-8">
<title>Breezy Acorn Company – Sea Salt Chunky Label</title>
<link rel="stylesheet" href="https://fonts.googleapis.com/css2?family=Advent+Pro:wght@300;400&family=Bungee&family=Roboto+Condensed:wght@400&family=Arimo:wght@700&display=swap">
<style>
  :root {
    --paper: #ffffff;
    --teal: #2a8bbf;
    --orange: #f05a28;
    --ink: #000000;
    --grey-light: #c9c9c9;
    --grey-mid: #a3a3a3;
    --glue-grey: #bcbcbc;
  }
  * { margin: 0; padding: 0; box-sizing: border-box; }
  html, body { width: 1200px; height: 708px; overflow: hidden; background: var(--paper); }
  .label {
    position: relative;
    width: 1200px;
    height: 708px;
    background: var(--paper);
    border: 1px solid #e6e6e6;
    overflow: hidden;
  }
  .glue-strip {
    position: absolute;
    left: 0; top: 0;
    width: 68px; height: 708px;
    border-right: 4px dashed var(--ink);
  }
  .glue-strip__text {
    position: absolute;
    left: 34px; top: 354px;
    transform: translate(-50%, -50%) rotate(-90deg);
    white-space: nowrap;
    font-family: "Arimo", Arial, sans-serif;
    font-weight: 700;
    font-size: 50px;
    letter-spacing: 3px;
    color: var(--glue-grey);
    -webkit-text-stroke: 1px #8c8c8c;
  }
  .brand {
    position: absolute;
    font-family: "Advent Pro", sans-serif;
    font-weight: 300;
    line-height: 1;
  }
  .brand__first {
    left: 150px; top: 10px;
    font-size: 148px;
    color: var(--teal);
  }
  .brand__second {
    left: 150px; top: 150px;
    width: 460px;
    text-align: right;
    font-size: 196px;
    color: var(--teal);
  }
  .brand__company {
    left: 205px; top: 340px;
    font-size: 100px;
    font-weight: 400;
    color: var(--orange);
  }
  .flavour {
    position: absolute;
    left: 158px; top: 449px;
    width: 471px; height: 81px;
    border-radius: 40px;
    background: var(--teal);
    color: var(--paper);
    font-family: "Advent Pro", sans-serif;
    font-weight: 300;
    font-size: 86px;
    line-height: 81px;
    text-align: center;
    letter-spacing: 2px;
  }
  .texture {
    position: absolute;
    left: 158px; top: 539px;
    width: 474px; height: 153px;
  }
  .texture text {
    font-family: "Bungee", sans-serif;
    fill: var(--orange);
  }
  .health-panel {
    position: absolute;
    left: 706px; top: 32px;
    width: 452px; height: 349px;
    border: 5px solid var(--ink);
    border-radius: 36px;
    display: flex;
    flex-direction: column;
    align-items: center;
    justify-content: center;
    font-family: "Roboto Condensed", sans-serif;
    font-size: 132px;
    line-height: 1.1;
    color: var(--grey-light);
    text-align: center;
  }
  .trademark-panel {
    position: absolute;
    left: 724px; top: 404px;
    width: 434px; height: 189px;
    border: 2px solid var(--ink);
    display: flex;
    align-items: center;
    justify-content: center;
    font-family: "Arimo", Arial, sans-serif;
    font-weight: 700;
    font-size: 30px;
    line-height: 1.45;
    color: var(--grey-mid);
    text-align: center;
  }
</style>
</head>
<body>
  <main class="label">
    <div class="glue-strip">
      <span class="glue-strip__text">OVERLAP FOR GLUE</span>
    </div>

    <h1 class="brand-block">
      <span class="brand brand__first">Breezy</span>
      <span class="brand brand__second">Acorn</span>
      <span class="brand brand__company">company</span>
    </h1>

    <p class="flavour">SEA SALT</p>

    <svg class="texture" viewBox="0 0 474 153" aria-label="Chunky">
      <text x="0" y="150" font-size="160" textLength="474" lengthAdjust="spacingAndGlyphs">CHUNKY</text>
    </svg>

    <div class="health-panel">
      <span>HEALTH</span>
      <span>INFO</span>
    </div>

    <div class="trademark-panel">
      <p>Company an<br>Trademark info<br>will go here</p>
    </div>
  </main>
</body>
</html>
```